Mushroom Packaging - will require space for UPC code and other disclosures.

We are seeking to make packaging labels for our mushrooms.

Target Market(s)

Retail packaging label - there will be 20 different labels. We wish assistance on many different iterations changing the words and colors to differentiat new products

Industry/Entity Type

Retail mushroom packaging

Logo Text

Brand name is Meadow and Plate - space for label specifics as shown in examples

Logo styles of interest
Pictorial/Combination Logo
Requirements
Must have
• Must be a 2 inch by 3 inch label and must say product of USA, keep refridgerated, Make the name of the products most important part
Nice to have
• Ability to work with deisgner after the project is complete.
Should not have
• small fonts for the type of product. Please start with Sliced Shiitake Mushrooms Later we will add varations for other types such as Crimini Portabella Shiitake Oyster King Trumpets

```html
<!DOCTYPE html>
<html lang="en">
<head>
<meta charset="utf-8">
<title>Meadow and Plate – Sliced Shiitake Mushrooms Label</title>
<link rel="stylesheet" href="https://fonts.googleapis.com/css2?family=Outfit:ital,wght@0,400;0,500;0,600;0,700;1,500&display=swap">
<style>
  :root {
    --bg: #fdf0e0;
    --label-cream: #fffbee;
    --label-orange: #fbb751;
    --badge-shadow: #f7a33c;
    --badge-red: #a83226;
    --text-brown: #7a2416;
    --text-red: #a83226;
    --band-peach: #fde1b4;
  }
  html, body {
    margin: 0;
    padding: 0;
    overflow: hidden;
  }
  .canvas {
    width: 842px;
    height: 1200px;
    background: var(--bg);
    position: relative;
    overflow: hidden;
  }
  .label {
    position: absolute;
    left: 50%;
    top: 318px;
    width: 760px;
    height: 564px;
    transform: translateX(-50%);
    font-family: "Outfit", sans-serif;
  }
  .label-shape { fill: var(--label-cream); stroke: var(--label-orange); stroke-width: 24; }
  .badge-shadow { fill: var(--badge-shadow); }
  .badge { fill: var(--badge-red); }
  .brand-name { fill: var(--label-cream); font-weight: 700; font-size: 34px; }
  .storage-band { fill: var(--band-peach); }
  .storage-note { fill: var(--text-red); font-style: italic; font-weight: 500; font-size: 19px; }
  .product-name { fill: var(--text-brown); font-weight: 600; font-size: 52px; }
  .product-type { fill: var(--label-orange); font-weight: 500; font-size: 24px; letter-spacing: 6px; }
  .origin-tab { fill: var(--label-orange); }
  .origin-note { fill: var(--text-brown); font-weight: 600; font-size: 26px; }
</style>
</head>
<body>
<div class="canvas">
  <svg class="label" viewBox="-15 -15 650 485" xmlns="http://www.w3.org/2000/svg">
    <path class="label-shape" d="M 110,455 C 40,455 0,400 0,300 C 0,190 70,125 150,125 C 160,50 230,0 310,0 C 390,0 460,50 470,125 C 550,125 620,190 620,300 C 620,400 580,455 510,455 Z"/>

    <path class="storage-band" d="M 365,268 L 410,205 L 600,205 L 600,268 Z"/>
    <text class="storage-note" x="562" y="228" text-anchor="end">Keep</text>
    <text class="storage-note" x="562" y="256" text-anchor="end">Refridgerated</text>

    <g class="brand">
      <circle class="badge-shadow" cx="324" cy="162" r="110"/>
      <circle class="badge" cx="310" cy="155" r="108"/>
      <text class="brand-name" x="310" y="145" text-anchor="middle">Meadow</text>
      <text class="brand-name" x="310" y="185" text-anchor="middle">and Plate</text>
    </g>

    <text class="product-name" x="308" y="335" text-anchor="middle">Sliced Shiitake</text>
    <text class="product-type" x="311" y="376" text-anchor="middle">MUSHROOMS</text>

    <path class="origin-tab" d="M 160,448 C 175,420 180,398 205,398 L 415,398 C 440,398 445,420 460,448 Z"/>
    <text class="origin-note" x="310" y="434" text-anchor="middle">Product Of USA</text>
  </svg>
</div>
</body>
</html>
```